Professional and Fun Business Cards for #1 Lagoon Care

We want an updated look for our existing business cards. In addition, we need to update the logos on the back side of the card to be the most current award for Brevin's Ledger. I have an eps of the Brevin's Ledger award logo but it is too big to upload here, so I can email it to the designer once selected.

Target Market(s)

Families with swimming pools

Industry/Entity Type

Business

Contact Information for Business Card

Thomas Garvey
Partner & Senior Pool Technician
Garvey & Kin Pool Service, Inc.
2460 Marlow Avenue, Suite 310
Elmbrook, CA 95799
(916) 555-0143 service
(916) 555-0187 billing
info@garvey-kin.example
www.garvey-kin.example

Font styles to use
Other font styles liked:
• Goudy Sans Bold

Colors
3176b5
34a7d8
34b8a4
add136

Requirements
Must have
• Garvey & Kin logo and contact information on the front
• All other logos on the back
Nice to have
• Open to ideas...
Should not have
• Can't think of anything specific

```html
<!DOCTYPE html>
<html lang="en">
<head>
<meta charset="utf-8">
<title>Garvey &amp; Kin Pool Service – Business Card</title>
<link rel="stylesheet" href="https://fonts.googleapis.com/css2?family=Alegreya+Sans:wght@700;800&display=swap">
<style>
  :root {
    --lime: #add136;
    --navy: #3176b5;
    --sky: #34a7d8;
    --teal: #34b8a4;
    --ink: #111111;
  }
  html, body {
    margin: 0;
    padding: 0;
    width: 1200px;
    height: 686px;
    overflow: hidden;
    background: #ffffff;
  }
  .card {
    position: relative;
    width: 1200px;
    height: 686px;
    overflow: hidden;
    background: var(--lime);
    font-family: "Alegreya Sans", "Trebuchet MS", sans-serif;
    font-weight: 700;
    color: var(--ink);
  }
  .waves {
    position: absolute;
    inset: 0;
    width: 1200px;
    height: 686px;
  }
  .brand {
    position: absolute;
    left: 0;
    width: 1160px;
    top: 112px;
    margin: 0;
    text-align: center;
    font-size: 92px;
    font-weight: 800;
    line-height: 1;
    color: var(--navy);
  }
  .brand-dot {
    display: inline-block;
    width: 40px;
    height: 40px;
    border-radius: 50%;
    background: var(--sky);
    vertical-align: middle;
    margin-right: 18px;
    position: relative;
    top: -6px;
  }
  .holder {
    position: absolute;
    left: 0;
    width: 1220px;
    top: 250px;
    margin: 0;
    text-align: center;
    font-size: 37px;
    line-height: 47px;
  }
  .phones {
    position: absolute;
    left: 0;
    width: 1188px;
    top: 482px;
    margin: 0;
    text-align: center;
    font-size: 44px;
    letter-spacing: 0.3px;
  }
  .address, .online {
    position: absolute;
    top: 562px;
    margin: 0;
    font-size: 30px;
    line-height: 47px;
    font-style: normal;
  }
  .address { left: 32px; }
  .online { right: 36px; text-align: right; }
</style>
</head>
<body>
<main class="card">
  <svg class="waves" viewBox="0 0 1200 686" aria-hidden="true">
    <defs>
      <linearGradient id="shallows" x1="0" y1="0" x2="0" y2="1">
        <stop offset="0" stop-color="#c3e9e4"/>
        <stop offset="1" stop-color="#2db8a0"/>
      </linearGradient>
    </defs>
    <path d="M0 318 C200 300 360 345 600 336 S1000 300 1200 316 L1200 480 L0 480 Z" fill="var(--teal)"/>
    <path d="M0 336 C250 322 450 362 700 350 S1050 322 1200 332 L1200 480 L0 480 Z" fill="var(--navy)"/>
    <path d="M0 372 C230 358 480 398 740 384 S1050 364 1200 378 L1200 480 L0 480 Z" fill="var(--sky)"/>
    <path d="M0 404 C300 392 600 426 860 414 S1100 402 1200 412 L1200 480 L0 480 Z" fill="var(--navy)"/>
    <path d="M0 442 C320 430 700 464 1200 452 L1200 686 L0 686 Z" fill="url(#shallows)" stroke="var(--lime)" stroke-width="2"/>
  </svg>

  <h1 class="brand"><span class="brand-dot"></span>Garvey &amp; Kin</h1>

  <p class="holder">Thomas Garvey Partner &amp; Senior Pool Technician<br>Garvey &amp; Kin Pool Service, Inc.</p>

  <p class="phones">(916) 555-0143 service (916) 555-0187</p>

  <address class="address">
    2460 Marlow Avenue, Suite 310<br>
    Elmbrook, CA 95799
  </address>

  <p class="online">
    billing info@garvey-kin.example<br>
    www.garvey-kin.example
  </p>
</main>
</body>
</html>
```